Stationary Design for Stunning new Logo

I need to envelopes, letterhead, business cards designed to compliment our new logo.

We are a 25 year old printing company going through a brand refresh. All items should have the design extended to both sides for full print ability.

Industry/Entity Type

Printing

Requirements
Must have
• It must utilize the new logo & colors PMS 300 & PMS 295.

```html
<!DOCTYPE html>
<html lang="en">
<head>
<meta charset="utf-8">
<title>Northmark Envelope Set</title>
<link href="https://fonts.googleapis.com/css2?family=Open+Sans:wght@400;600;700&display=swap" rel="stylesheet">
<style>
  :root {
    --stage: #c3c8cc;
    --paper: #ffffff;
    --pms-300: #1a6fd6;
    --pms-295: #063f8f;
    --ink: #1c1c1c;
    --shadow: rgba(0, 0, 0, 0.28);
  }
  html, body {
    margin: 0;
    padding: 0;
    overflow: hidden;
  }
  body {
    width: 1200px;
    height: 848px;
    background: var(--stage);
    position: relative;
    font-family: "Open Sans", Arial, sans-serif;
  }
  .envelope {
    position: absolute;
    background: var(--paper);
    box-shadow: 3px 4px 8px var(--shadow);
    overflow: hidden;
  }
  /* Front face */
  .envelope--front {
    left: 110px;
    top: 90px;
    width: 690px;
    height: 300px;
  }
  .envelope--front .base-band {
    position: absolute;
    left: 0;
    right: 0;
    bottom: 0;
    height: 16px;
    background: linear-gradient(90deg, var(--pms-295), var(--pms-300));
  }
  .return-block {
    position: absolute;
    left: 30px;
    top: 28px;
  }
  .brand {
    display: flex;
    align-items: center;
    gap: 6px;
  }
  .brand__dot {
    width: 18px;
    height: 18px;
    border-radius: 50%;
    background: var(--pms-300);
  }
  .brand__name {
    font-weight: 700;
    font-size: 24px;
    letter-spacing: 0.5px;
    color: var(--pms-300);
    line-height: 1;
  }
  .brand__tagline {
    margin: 3px 0 10px 24px;
    font-size: 5.5px;
    font-weight: 600;
    letter-spacing: 0.3px;
    color: var(--pms-300);
    text-transform: uppercase;
  }
  .return-address {
    margin: 0 0 0 24px;
    font-style: normal;
    font-size: 12.5px;
    font-weight: 600;
    line-height: 1.3;
    color: var(--ink);
  }
  /* Back face */
  .envelope--back {
    left: 385px;
    top: 424px;
    width: 685px;
    height: 345px;
  }
  .envelope--back svg {
    position: absolute;
    inset: 0;
  }
  .web-address {
    position: absolute;
    left: 0;
    right: 0;
    top: 76px;
    text-align: center;
    font-size: 10px;
    font-weight: 700;
    color: var(--paper);
  }
</style>
</head>
<body>

  <section class="envelope envelope--front" aria-label="Envelope front">
    <div class="return-block">
      <div class="brand">
        <span class="brand__dot"></span>
        <span class="brand__name">NORTHMARK</span>
      </div>
      <p class="brand__tagline">Fast Service • Fine Product • Fair Pricing</p>
      <address class="return-address">
        Northmark, Inc. 2715<br>
        Alder Commerce Way<br>
        Fairview, GA 30512
      </address>
    </div>
    <div class="base-band"></div>
  </section>

  <section class="envelope envelope--back" aria-label="Envelope back">
    <svg width="685" height="345" viewBox="0 0 685 345" aria-hidden="true">
      <defs>
        <linearGradient id="frameTone" x1="0" y1="0" x2="1" y2="0">
          <stop offset="0" stop-color="#1f62d8"/>
          <stop offset="0.45" stop-color="#2a7ff0"/>
          <stop offset="0.6" stop-color="#0e3fbf"/>
          <stop offset="1" stop-color="#1a5fe0"/>
        </linearGradient>
      </defs>
      <rect x="0" y="0" width="685" height="345" fill="url(#frameTone)"/>
      <rect x="15" y="15" width="652" height="312" fill="#ffffff"/>
      <path d="M0 0 H685 V8 C640 30 560 62 470 88 C420 102 380 122 345 123 C310 124 270 104 215 88 C130 62 50 30 0 8 Z" fill="var(--pms-295)"/>
    </svg>
    <p class="web-address">www.northmark-inc.com</p>
  </section>

</body>
</html>
```